Plastering (solid plastering) business card design

We need a business card for a a small plastering business based in Perth Western Australia. We are a small team that provides a service in solid plastering specialising in float, white set and sand finish. We would like to see a clean business card with our name "Ridgeline Render Co" being the focus of the card and maybe incorporated into a logo. We don't have a logo at the moment so we would like to see some cards that may provide us with our future logo.

Industry/Entity Type

Business

Contact Information for Business Card

Ridgeline Render Co

Solid Plastering Specialists

Ph: Corey 0418730615
Ph: Luke 0451082963

Requirements
Should not have
• The design should not have Drywall incorporated into the card. In perth W.A. Plastering in different to someone that puts up Panelmax. We use sand, cement, lime and hardwall plaster.

```html
<!DOCTYPE html>
<html lang="en">
<head>
<meta charset="utf-8">
<title>Ridgeline Render Co — Business Card</title>
<link rel="stylesheet" href="https://fonts.googleapis.com/css2?family=Exo+2:wght@400;600&display=swap">
<style>
  :root {
    --backdrop-light: #e4e4e4;
    --backdrop-dark: #bdbdbd;
    --card: #ffffff;
    --panel: #ececec;
    --brand-blue: #1ba4dd;
    --ink: #2b2b2b;
    --ink-soft: #8a8a8a;
    --tagline: #7a7a7a;
    --rule: #9a9a9a;
  }
  * { box-sizing: border-box; margin: 0; padding: 0; }
  html, body { width: 1200px; height: 949px; overflow: hidden; }
  body {
    background: radial-gradient(ellipse at 45% 40%, var(--backdrop-light), var(--backdrop-dark));
    font-family: "Exo 2", Arial, sans-serif;
    color: var(--ink);
    position: relative;
  }
  .card {
    position: absolute;
    width: 560px;
    height: 320px;
    background: var(--card);
    border-radius: 18px;
    overflow: hidden;
    box-shadow: 0 14px 30px rgba(0,0,0,.22);
  }
  .card--back { left: 90px; top: 110px; }
  .card--front { left: 550px; top: 510px; }

  .brand-name {
    font-weight: 600;
    color: var(--brand-blue);
    letter-spacing: .5px;
    line-height: 1;
  }
  .tagline {
    font-weight: 400;
    color: var(--tagline);
    letter-spacing: 3px;
    line-height: 1;
  }
  .card--back .brand-block {
    position: absolute; left: 0; right: 0; top: 118px; text-align: center;
  }
  .card--back .brand-name { font-size: 38px; }
  .card--back .tagline { font-size: 17px; margin-top: 10px; }

  .social {
    position: absolute;
    right: 26px; bottom: 22px;
    display: flex; align-items: center; gap: 12px;
    font-size: 14px; color: var(--ink-soft);
  }
  .social__dot { width: 14px; height: 14px; border-radius: 50%; background: var(--ink-soft); }

  .card--front .brand-block { position: absolute; left: 36px; top: 24px; }
  .card--front .brand-name { font-size: 30px; }
  .card--front .tagline { font-size: 14px; margin-top: 6px; letter-spacing: 2.5px; }

  .holder {
    position: absolute; left: 36px; top: 96px;
    display: flex; align-items: center; gap: 10px;
    font-size: 14px; font-weight: 600; letter-spacing: 1px;
  }
  .holder__role { font-weight: 400; letter-spacing: .5px; margin-left: 14px; }

  .contact {
    position: absolute; left: 0; right: 0; top: 128px; bottom: 0;
    background: linear-gradient(90deg, var(--card) 0%, var(--panel) 55%);
  }
  .contact__accent {
    position: absolute; left: 0; top: 0; bottom: 0; width: 38px;
    background: var(--brand-blue);
  }
  .contact__row {
    position: absolute; left: 38px; right: 0; height: 48px;
    display: flex; align-items: center; gap: 16px;
    padding-left: 28px;
    border-top: 1px solid var(--rule);
    font-size: 16px;
    line-height: 1.2;
  }
  .contact__row:nth-child(2) { top: 0; }
  .contact__row:nth-child(3) { top: 48px; }
  .contact__row:nth-child(4) { top: 96px; font-size: 15px; }
  .contact__row:nth-child(5) { top: 144px; font-size: 15px; }
  .contact__label { display: inline-block; width: 52px; color: var(--ink-soft); }
  .icon { width: 20px; height: 20px; flex: none; fill: var(--ink-soft); }
  .icon--line { fill: none; stroke: var(--ink-soft); stroke-width: 1.5; }
</style>
</head>
<body>

<section class="card card--back" aria-label="Card back">
  <div class="brand-block">
    <div class="brand-name">Ridgeline Render Co</div>
    <div class="tagline">Solid Plastering Specialists</div>
  </div>
  <div class="social">
    <span>like</span>
    <span class="social__dot"></span>
    <span class="social__dot"></span>
  </div>
</section>

<section class="card card--front" aria-label="Card front">
  <div class="brand-block">
    <div class="brand-name">Ridgeline Render Co</div>
    <div class="tagline">Solid Plastering Specialists</div>
  </div>
  <div class="holder">
    <svg class="icon" viewBox="0 0 20 20" style="fill:var(--ink)"><circle cx="10" cy="6" r="4"/><path d="M2 19c0-5 3.5-7 8-7s8 2 8 7z"/></svg>
    <span>COREY &amp; LUKE</span><span class="holder__role">founders</span>
  </div>
  <div class="contact">
    <div class="contact__accent"></div>
    <div class="contact__row">
      <svg class="icon" viewBox="0 0 20 20"><path d="M4 2l3 0 2 4-2 2c1 2 3 4 5 5l2-2 4 2 0 3c0 1-1 2-2 2C9 18 2 11 2 4c0-1 1-2 2-2z"/></svg>
      <span><span class="contact__label">Corey</span>0418 730 615<br><span class="contact__label">Luke</span>0451 082 963</span>
    </div>
    <div class="contact__row">
      <svg class="icon icon--line" viewBox="0 0 20 20"><path d="M1 4h18v12H1z M2 5l8 6 8-6"/></svg>
      <span>hello@ridgelinerender.com</span>
    </div>
    <div class="contact__row">
      <svg class="icon icon--line" viewBox="0 0 20 20"><circle cx="10" cy="10" r="8"/><ellipse cx="10" cy="10" rx="3.5" ry="8"/><path d="M2 10h16M4 5h12M4 15h12"/></svg>
      <span>www.ridgelinerender.com</span>
    </div>
    <div class="contact__row">
      <svg class="icon" viewBox="0 0 20 20"><path d="M10 1a6 6 0 0 1 6 6c0 5-6 12-6 12S4 12 4 7a6 6 0 0 1 6-6zm0 3.5a2.5 2.5 0 1 0 0 5 2.5 2.5 0 0 0 0-5z"/></svg>
      <span>14 Kestrel Lane, Level 2<br>Osborne Park WA</span>
    </div>
  </div>
</section>

</body>
</html>
```